Assorted Banner Ads

Create standard sized banner ads (300x250, 728x90, 160x600) using logo and create exciting ads using collateral provided and your own ideas.

```html
<!DOCTYPE html>
<html lang="en">
<head>
<meta charset="utf-8">
<title>Tidewater Quest – Banner Set</title>
<link rel="stylesheet" href="https://fonts.googleapis.com/css2?family=Arimo:wght@400;700&family=Kaushan+Script&display=swap">
<style>
  :root{
    --page:#e4e6e9;
    --orange:#e8600c;
    --green:#1f8a3c;
    --ink:#111111;
    --white:#ffffff;
    --wood-dark:#3a1e0c;
    --wood-mid:#7a4119;
    --wood-light:#c07a3a;
  }
  *{box-sizing:border-box;margin:0;padding:0}
  html,body{width:1200px;height:1200px;overflow:hidden}
  body{background:var(--page);font-family:"Arimo",Arial,sans-serif;position:relative}

  .banner{position:absolute;overflow:hidden;background:var(--orange);box-shadow:0 2px 6px rgba(0,0,0,.25)}
  .banner--skyscraper{left:196px;top:12px;width:250px;height:942px}
  .banner--rectangle{left:508px;top:510px;width:538px;height:446px}
  .banner--leaderboard{left:54px;top:1008px;width:1096px;height:132px}

  .scene-photo{position:absolute;inset:0;
    background:
      radial-gradient(ellipse at 50% 20%, rgba(230,150,70,.55), transparent 60%),
      linear-gradient(180deg,var(--wood-mid) 0%,var(--wood-dark) 45%,var(--wood-mid) 75%,var(--wood-light) 100%)}

  .swoosh{position:absolute;left:0;width:100%;display:block}

  .brand-tab{position:absolute;top:0;background:var(--white);border:4px solid var(--green);border-top:none;
    border-radius:0 0 60px 60px;display:flex;align-items:center;justify-content:center;z-index:3}
  .brand-tab__name{font-weight:700;color:var(--ink);text-align:center;white-space:nowrap;font-size:15px}

  .title{position:absolute;font-family:"Kaushan Script",cursive;color:var(--white);text-align:center;
    -webkit-text-stroke:2px var(--ink);paint-order:stroke fill;text-shadow:2px 3px 3px rgba(0,0,0,.6);z-index:2;line-height:1.05}
  .question{position:absolute;color:var(--white);font-weight:700;text-align:center;text-transform:uppercase;
    text-shadow:1px 2px 3px rgba(0,0,0,.6);z-index:2;line-height:1.2}

  .phone-pill{position:absolute;display:flex;align-items:center;justify-content:center;gap:10px;border-radius:20px;
    background:linear-gradient(90deg,#000 0%,#3b3b3b 50%,#000 100%);color:var(--white);font-weight:700;z-index:2}
  .phone-pill svg{flex:none}
  .site-url{position:absolute;color:var(--white);font-weight:700;text-align:center;z-index:2}

  /* skyscraper */
  .banner--skyscraper .brand-tab{left:50px;width:150px;height:112px}
  .banner--skyscraper .title{left:0;right:0;top:330px;font-size:44px}
  .banner--skyscraper .question{left:0;right:0;top:656px;font-size:25px}
  .banner--skyscraper .swoosh{top:790px;height:152px}
  .banner--skyscraper .phone-pill{left:8px;width:234px;top:860px;height:30px;font-size:15px}
  .banner--skyscraper .site-url{left:0;right:0;top:908px;font-size:15px}

  /* rectangle */
  .banner--rectangle .brand-tab{left:2px;width:146px;height:100px}
  .banner--rectangle .title{left:40px;right:0;top:130px;font-size:40px}
  .banner--rectangle .question{left:40px;right:0;top:206px;font-size:28px}
  .banner--rectangle .swoosh{top:300px;height:146px}
  .banner--rectangle .phone-pill{left:96px;width:348px;top:378px;height:30px;font-size:16px}
  .banner--rectangle .site-url{left:0;right:0;top:420px;font-size:17px}

  /* leaderboard */
  .banner--leaderboard .scene-photo{right:360px}
  .banner--leaderboard .swoosh{top:0;height:132px}
  .banner--leaderboard .brand-tab{left:22px;width:144px;height:124px;border-radius:0 0 56px 56px}
  .banner--leaderboard .title{left:170px;width:500px;top:22px;font-size:32px}
  .banner--leaderboard .question{left:170px;width:500px;top:80px;font-size:24px}
  .banner--leaderboard .phone-pill{left:762px;width:294px;top:44px;height:26px;font-size:14px}
  .banner--leaderboard .site-url{left:762px;width:294px;top:78px;font-size:15px}
</style>
</head>
<body>

<!-- 160x600 skyscraper -->
<section class="banner banner--skyscraper">
  <div class="scene-photo" role="img" aria-label="Warm-lit wooden pirate ship cabin with beams, ropes and lattice windows"></div>
  <div class="brand-tab"><span class="brand-tab__name">Tidewater Quest</span></div>
  <h2 class="title">Pirate<br>Treasure<br>Hunt</h2>
  <p class="question">Can you<br>escape in<br>60 minutes?</p>
  <svg class="swoosh" viewBox="0 0 250 152" preserveAspectRatio="none" aria-hidden="true">
    <path d="M0 10 Q125 -8 250 18 L250 152 L0 152 Z" fill="var(--green)"/>
    <path d="M0 14 Q125 -2 250 24 L250 152 L0 152 Z" fill="var(--white)"/>
    <path d="M0 20 Q125 8 250 34 L250 152 L0 152 Z" fill="var(--ink)"/>
    <path d="M0 30 Q125 20 250 44 L250 152 L0 152 Z" fill="var(--white)"/>
    <path d="M0 38 Q125 30 250 50 L250 152 L0 152 Z" fill="var(--orange)"/>
  </svg>
  <div class="phone-pill">
    <svg width="18" height="18" viewBox="0 0 24 24" aria-hidden="true"><circle cx="12" cy="12" r="11" fill="none" stroke="#fff" stroke-width="2"/><path d="M8 6.5l2 0 1 3-1.5 1.2a8 8 0 0 0 3.8 3.8L14.5 13l3 1v2c0 .8-.7 1.5-1.5 1.5A10 10 0 0 1 6.5 8c0-.8.7-1.5 1.5-1.5z" fill="#fff"/></svg>
    <span>555-014-2290</span>
  </div>
  <p class="site-url">tidewaterquest.com</p>
</section>

<!-- 300x250 rectangle -->
<section class="banner banner--rectangle">
  <div class="scene-photo" role="img" aria-label="Warm-lit wooden pirate ship cabin with curved beams, ropes, a table and lattice windows"></div>
  <div class="brand-tab"><span class="brand-tab__name">Tidewater Quest</span></div>
  <h2 class="title">Pirate Treasure Hunt</h2>
  <p class="question">Can you escape in<br>60 minutes?</p>
  <svg class="swoosh" viewBox="0 0 538 146" preserveAspectRatio="none" aria-hidden="true">
    <path d="M0 14 Q270 -12 538 10 L538 146 L0 146 Z" fill="var(--green)"/>
    <path d="M0 18 Q270 -6 538 16 L538 146 L0 146 Z" fill="var(--white)"/>
    <path d="M0 26 Q270 4 538 28 L538 146 L0 146 Z" fill="var(--ink)"/>
    <path d="M0 38 Q270 18 538 40 L538 146 L0 146 Z" fill="var(--white)"/>
    <path d="M0 48 Q270 28 538 50 L538 146 L0 146 Z" fill="var(--orange)"/>
  </svg>
  <div class="phone-pill">
    <svg width="18" height="18" viewBox="0 0 24 24" aria-hidden="true"><circle cx="12" cy="12" r="11" fill="none" stroke="#fff" stroke-width="2"/><path d="M8 6.5l2 0 1 3-1.5 1.2a8 8 0 0 0 3.8 3.8L14.5 13l3 1v2c0 .8-.7 1.5-1.5 1.5A10 10 0 0 1 6.5 8c0-.8.7-1.5 1.5-1.5z" fill="#fff"/></svg>
    <span>555-014-2290</span>
  </div>
  <p class="site-url">tidewaterquest.com</p>
</section>

<!-- 728x90 leaderboard -->
<section class="banner banner--leaderboard">
  <div class="scene-photo" role="img" aria-label="Warm-lit wooden pirate ship cabin interior panorama"></div>
  <svg class="swoosh" viewBox="0 0 1096 132" preserveAspectRatio="none" aria-hidden="true">
    <path d="M650 0 Q720 66 670 132 L1096 132 L1096 0 Z" fill="var(--green)"/>
    <path d="M656 0 Q728 66 678 132 L1096 132 L1096 0 Z" fill="var(--white)"/>
    <path d="M664 0 Q738 66 690 132 L1096 132 L1096 0 Z" fill="var(--ink)"/>
    <path d="M676 0 Q752 66 704 132 L1096 132 L1096 0 Z" fill="var(--white)"/>
    <path d="M686 0 Q762 66 714 132 L1096 132 L1096 0 Z" fill="var(--orange)"/>
  </svg>
  <div class="brand-tab"><span class="brand-tab__name">Tidewater Quest</span></div>
  <h2 class="title">Pirate Treasure Hunt</h2>
  <p class="question">Can you escape in 60 minutes?</p>
  <div class="phone-pill">
    <svg width="16" height="16" viewBox="0 0 24 24" aria-hidden="true"><circle cx="12" cy="12" r="11" fill="none" stroke="#fff" stroke-width="2"/><path d="M8 6.5l2 0 1 3-1.5 1.2a8 8 0 0 0 3.8 3.8L14.5 13l3 1v2c0 .8-.7 1.5-1.5 1.5A10 10 0 0 1 6.5 8c0-.8.7-1.5 1.5-1.5z" fill="#fff"/></svg>
    <span>555-014-2290</span>
  </div>
  <p class="site-url">tidewaterquest.com</p>
</section>

</body>
</html>
```